Bifold brochure design for leadership academy

Please see below. This is a bifold brochure for a leadership academy. (www.vesk.institute). Look and feel must be colours, shapes, abstract designs, graphics, pictures. Make this professional, yet casual and bold.

Feel free to design just the front and back cover, then I'll give feedback on whether or not you're in the right direction.

COVER
- Title: “The Brightwater Year Journey”
- “Northmere Pathways Institute” logo somewhere
- Subtitles (with images, icons, and/or shapes): “Self-discovery” “Skills development” “Real-world Impact”

PAGE 2 (Inside Fold)
- Title: "The Program"
- Section 2a: Section title: "How it works”
- Image: See website, image under "four phases of the program". Please adapt and make it look better
- Text: VPI is a structured, 8-month ‘gap year’ program for 18-25 year olds who want more than just a year off – they want a year ahead. Our aim is to develop high-potential young leaders with strong values, clear purpose, high-impact skills, and a track record of real-world accomplishments that are second-to-none. We do this through four-phases.
- Section 2b: Section title: “Dates & Timing”
- Image: See image on website under 'dates and timing'. Make sure both dates show up on the brochure (September and January program).
- Text: There are two programs per year: one that starts in September, the other in January. The first four months of the program are based in Toronto at the VPI headquarters. The curriculum we work through is highly engaging and personalized, focusing directly on students’ goals. After that, students are out in the world, achieving the remaining components of the program (e.g. internship, volunteer abroad).

PAGE 3 (Outside Fold)
- Page Title: "The Students"
- Section 3a: Section title: “Who’s it for”
- Subtitle1: “High school graduates”
 Image/icon of a high school grad
 Text1: 90% of high school grads aren't sure why they’re going to university or what they want to study.
 Text2: VPI helps students discover what they truly want to do in life, and make enormous progress towards these goals.

- Subtitle2: “Post-secondary students”
 Image/icon of a university / college student
 Text1: 28% of students switch or drop out of their program because it wasn’t for them or they didn’t like it.
 Text2: Don't keep moving around or risk switching careers down the road – find out what sparks your passion with VPI.

- Subtitle3: “Post-secondary graduates”
 Image/icon of a university/ college grad
 Text1: 50% of graduates are unemployed or underemployed, 60% are in debt.
 Text2: VPI will help you get your dream job – our students won’t settle for anything less.

- Section 3b: Section title: “How to apply”
 Text1: We select high-potential young leaders with a desire to improve themselves and impact the world.
 Text2: We won’t ask you for your grades – we care more about your values and potential.
 Text3: Visit www.vesk.institute to apply now

BACK COVER
- Page Title: “Get in Touch”
- Website: www.vesk.institute
- Facebook page: facebook.com/vesk.institute
- Twitter handle: @vesk_institute
- Email: marta@vesk.institute

Target Market(s)

18-25 year olds, parents, teachers

Industry/Entity Type

Leadership

Requirements
Must have
• Beautiful design - sleek and bold, yet colourful and casual. Keep the colours similar to our website (www.vesk.institute). See examples of other brochures.
• http://img.plorvex.net/jpg/00/11/22/33/240_F_11223344_aBcDeFgHiJkLmNoPqRsTuVwXyZ123456.jpg
• http://quandrelhub.com/wp-content/uploads/2014/11/Real-Estate-Bi-fold-Brochure.jpg
• http://www.trovanic.com/media/k2/galleries/5/001-bi-fold-brochure-psd-mock-up-template.jpg
• http://img.plorvex.net/jpg/00/44/55/66/240_F_44556677_zYxWvUtSrQpOnMlKjIhGfEdCbA987654.jpg

```html
<!DOCTYPE html>
<html lang="en">
<head>
<meta charset="utf-8">
<title>VPI Bifold Brochure – Inside Spread</title>
<link rel="stylesheet" href="https://fonts.googleapis.com/css2?family=Arimo:wght@400;700&display=swap">
<style>
:root{
  --bg:#e4e5e7;
  --paper:#ffffff;
  --yellow:#f2e500;
  --yellow-soft:#f5ec5c;
  --yellow-pale:#f7f29a;
  --yellow-deep:#e9dc3e;
  --red:#b31a1a;
  --red-dark:#9e1515;
  --ink:#1b1b1b;
  --grey:#555555;
  --teal:#3f9ac0;
  --frame:#3c3a8e;
}
*{margin:0;padding:0;box-sizing:border-box}
html,body{width:1200px;height:780px;overflow:hidden;background:var(--bg);font-family:"Arimo",Arial,sans-serif;color:var(--ink)}
.spread{position:absolute;left:55px;top:10px;width:1090px;height:755px;background:var(--paper);box-shadow:0 2px 8px rgba(0,0,0,.18)}
.page{position:absolute;top:25px;height:705px}
.page--program{left:25px;width:482px}
.page--students{left:507px;width:533px}
.shapes{position:absolute;left:0;top:0}
.page-title{position:absolute;top:2px;height:25px;background:var(--ink);color:#fff;font-weight:700;font-size:20px;line-height:25px;padding:0 10px}
.page--program .page-title{left:0;width:150px;clip-path:polygon(0 0,100% 0,94% 100%,0 100%)}
.page--students .page-title{right:0;width:190px;text-align:right;padding-right:12px}
.section-tag{position:absolute;left:0;top:33px;width:120px;height:20px;background:var(--red-dark);color:#fff;font-weight:700;font-size:14px;line-height:20px;padding-left:12px}
.phases-caption{position:absolute;left:120px;top:47px;color:#fff;font-size:6px;font-weight:700;letter-spacing:.2px}
.phase{position:absolute;width:115px;background:var(--yellow-soft)}
.phase__head{height:21px;background:var(--red);color:#fff;font-size:12px;line-height:21px;padding-left:6px}
.phase__art{position:absolute;border-radius:4px}
.phase__text{position:absolute;font-size:6.5px;line-height:11.5px;color:var(--ink)}
.phase__list{position:absolute;left:14px;top:100px;font-size:4.5px;line-height:9.5px;list-style:none;color:var(--ink)}
.phase__list li::before{content:"";display:inline-block;width:5px;height:5px;border-radius:50%;background:var(--red);margin-right:4px;vertical-align:middle;opacity:.7}
.intro{position:absolute;left:185px;top:313px;width:262px;font-size:10px;line-height:12px;text-align:justify;letter-spacing:.1px}
.dates-title{position:absolute;left:20px;top:432px;font-size:21px;font-weight:400;color:#222}
.timeline{position:absolute;left:5px;top:458px;width:300px;height:30px}
.timeline__months{position:absolute;left:0;top:14px;display:flex;font-size:8px;color:#333}
.timeline__months span{width:25px;text-align:center}
.timeline__label{position:absolute;top:0;font-size:3.5px;color:#333;text-align:center}
.timeline__line{position:absolute;top:8px;height:1px;background:#555}
.cal{position:absolute;top:427px;width:40px;height:37px;background:#fff;border-radius:3px;box-shadow:0 1px 2px rgba(0,0,0,.35)}
.cal::before{content:"";position:absolute;left:0;top:0;right:0;height:10px;background:var(--red);border-radius:3px 3px 0 0}
.cal span{position:absolute;left:0;right:0;top:18px;text-align:center;font-size:6px;color:#333}
.chart{position:absolute;left:3px;top:520px;width:282px;height:152px;background:#fff}
.chart__text{position:absolute;font-size:4px;color:#fff}
.chart__logo{position:absolute;left:9px;top:4px;font-size:6px;font-weight:700;color:var(--ink)}
.dates-text{position:absolute;left:321px;top:469px;width:158px;font-size:9.5px;line-height:11.6px;text-align:justify;letter-spacing:.2px}
.dates-text p+p{margin-top:12px}
.who-title{position:absolute;left:55px;top:60px;font-size:19px;font-weight:700;color:var(--teal);border-bottom:3px solid #1f6b6a;line-height:21px;width:123px}
.group-hs{position:absolute;left:72px;top:85px;font-size:13px;font-weight:400;color:var(--ink)}
.group-head{position:absolute;left:72px;font-size:20px;font-weight:400;color:#555}
.body{position:absolute;left:72px;width:300px;font-size:10.5px;line-height:12px;color:#333}
.photo{position:absolute;border:4px solid var(--frame)}
.apply-title{position:absolute;left:73px;top:513px;font-size:28px;font-weight:400;color:#2a2a2a}
.apply-mark{position:absolute;left:211px;top:506px;width:10px;height:10px;border-radius:50%;background:var(--ink)}
.apply-text{position:absolute;left:73px;font-size:8px;color:#222}
.badge{position:absolute;border-radius:2px}
</style>
</head>
<body>
<div class="spread">

  <section class="page page--program">
    <svg class="shapes" width="482" height="705" viewBox="0 0 482 705" aria-hidden="true">
      <rect x="0" y="0" width="482" height="398" fill="var(--yellow)"/>
      <polygon points="250,0 482,0 482,120 300,60" fill="var(--yellow-pale)"/>
      <polygon points="160,20 420,0 360,110" fill="var(--yellow-soft)"/>
      <polygon points="0,255 250,140 250,180 0,410" fill="var(--red)"/>
      <polygon points="60,398 482,230 482,398" fill="var(--yellow-pale)"/>
      <polygon points="175,305 482,270 482,398 175,398" fill="#faf6c0"/>
      <rect x="0" y="398" width="482" height="307" fill="var(--yellow-deep)"/>
      <polygon points="300,398 482,398 482,520" fill="var(--yellow-soft)"/>
    </svg>

    <div class="page-title">The Program</div>
    <div class="section-tag">How it works</div>
    <div class="phases-caption">FOUR PHASES OF THE PROGRAM</div>

    <div class="phase" style="left:2px;top:52px;height:200px">
      <div class="phase__head">1. Discover</div>
      <div class="phase__art" role="img" aria-label="Compass illustration" style="left:2px;top:26px;width:66px;height:66px;border-radius:50%;background:radial-gradient(#8ab7d8,#5b8fb8)"></div>
      <p class="phase__text" style="left:18px;top:94px;width:95px">Discover your strengths, development areas, personality style, passions and other attributes through a highly personalized transformation program.</p>
    </div>

    <div class="phase" style="left:123px;top:76px;height:160px">
      <div class="phase__head">2. Design</div>
      <div class="phase__art" role="img" aria-label="Goals worksheet illustration" style="left:3px;top:30px;width:42px;height:64px;background:linear-gradient(#e9e6d8,#cfcbb8)"></div>
      <p class="phase__text" style="left:56px;top:48px;width:58px">Design your year in the program and learn how to manage goals through our advanced goal-setting training.</p>
    </div>

    <div class="phase" style="left:245px;top:101px;height:155px">
      <div class="phase__head">3. Build</div>
      <div class="phase__art" role="img" aria-label="Presenter at whiteboard illustration" style="left:6px;top:26px;width:40px;height:34px;background:linear-gradient(#f4f1e6,#d9d3bf)"></div>
      <p class="phase__text" style="left:56px;top:58px;width:59px;line-height:10.5px">Build a set of skills that will directly help you achieve your goals, including issue-based problem solving, creativity, and structured communications.</p>
    </div>

    <div class="phase" style="left:365px;top:125px;height:160px">
      <div class="phase__head">4. Achieve</div>
      <div class="phase__art" role="img" aria-label="Achievement icons: question mark, medal, ticket, globe, flags" style="left:6px;top:26px;width:98px;height:42px;background:linear-gradient(90deg,#f1c760,#8fbfd9)"></div>
      <p class="phase__text" style="left:14px;top:74px;width:95px;font-size:5px;line-height:8px">Achieve six things before you can graduate:</p>
      <ul class="phase__list">
        <li>1. Solve a social problem</li>
        <li>2. Conquer a physical feat</li>
        <li>3. Organize an event</li>
        <li>4. Volunteer abroad</li>
        <li>5. Start something</li>
        <li>6. Do an internship</li>
      </ul>
    </div>

    <p class="intro">VPI is a structured, 8-month ‘gap year’ program for 18-25 year olds who want more than just a year off – they want a year ahead. Our aim is to develop high-potential young leaders with strong values, clear purpose, high-impact skills, and a track record of real-world accomplishments that are second-to-none. We do this through four-phases.</p>

    <h2 class="dates-title">Dates &amp; Timing</h2>
    <div class="timeline">
      <span class="timeline__label" style="left:0;width:22px">PREP WORK<br>ONLINE</span>
      <span class="timeline__label" style="left:35px;width:90px">FULL TIME IN CLASSROOM</span>
      <span class="timeline__label" style="left:140px;width:100px">MONTHLY CHECKPOINTS</span>
      <span class="timeline__line" style="left:0;width:22px"></span>
      <span class="timeline__line" style="left:28px;width:95px"></span>
      <span class="timeline__line" style="left:130px;width:115px"></span>
      <div class="timeline__months"><span>Aug</span><span>Sep</span><span>Oct</span><span>Nov</span><span>Dec</span><span>Jan</span><span>Feb</span><span>Mar</span><span>Apr</span><span>May</span><span>Jun</span><span>Jul</span></div>
    </div>
    <div class="cal" style="left:375px"><span>September</span></div>
    <div class="cal" style="left:418px"><span>January</span></div>

    <div class="chart">
      <svg width="282" height="152" viewBox="0 0 282 152" aria-hidden="true">
        <rect x="8" y="2" width="26" height="16" fill="#d8d8d8"/>
        <rect x="38" y="5" width="38" height="10" rx="2" fill="#6d8a3e"/>
        <circle cx="42" cy="24" r="7" fill="#c9a96a"/>
        <rect x="50" y="22" width="26" height="10" rx="2" fill="#6d8a3e"/>
        <circle cx="42" cy="46" r="8" fill="#3b66a8"/>
        <rect x="50" y="43" width="55" height="10" rx="2" fill="#3b66a8"/>
        <line x1="25" y1="18" x2="25" y2="130" stroke="#777" stroke-width="1"/>
        <rect x="140" y="48" width="5" height="10" fill="#2c3f98"/>
        <rect x="170" y="48" width="5" height="10" fill="#2c3f98"/>
        <rect x="200" y="48" width="5" height="10" fill="#2c3f98"/>
        <circle cx="42" cy="76" r="8" fill="#c0392b"/>
        <rect x="50" y="73" width="60" height="9" fill="#c0392b"/>
        <circle cx="42" cy="102" r="7" fill="#d98a2b"/>
        <rect x="50" y="99" width="75" height="9" fill="#c0392b"/>
        <rect x="36" y="120" width="18" height="12" fill="#6fb3d9"/>
        <rect x="54" y="122" width="55" height="9" fill="#c0392b"/>
        <circle cx="192" cy="82" r="8" fill="#c0392b"/>
        <rect x="200" y="79" width="70" height="9" fill="#c0392b"/>
        <circle cx="142" cy="104" r="8" fill="#c0392b"/>
        <rect x="150" y="101" width="65" height="9" fill="#c0392b"/>
        <circle cx="142" cy="128" r="8" fill="#c0392b"/>
        <rect x="150" y="125" width="75" height="9" fill="#c0392b"/>
      </svg>
      <span class="chart__logo" style="top:7px">VPI</span>
      <span class="chart__text" style="left:40px;top:7px">Find your purpose</span>
      <span class="chart__text" style="left:52px;top:24px">Design goals</span>
      <span class="chart__text" style="left:52px;top:45px">Build relevant skills</span>
      <span class="chart__text" style="left:54px;top:75px">Solve a social problem</span>
      <span class="chart__text" style="left:54px;top:101px">Conquer a physical feat</span>
      <span class="chart__text" style="left:58px;top:124px">Organize an Event</span>
      <span class="chart__text" style="left:205px;top:81px">Do an internship</span>
      <span class="chart__text" style="left:155px;top:103px">Volunteer abroad</span>
      <span class="chart__text" style="left:155px;top:127px">Start something</span>
      <span class="chart__text" style="left:140px;top:40px;color:#2c3f98">MONTHLY CHECKPOINTS</span>
    </div>

    <div class="dates-text">
      <p>There are two programs per year: one that starts in September, the other in January.</p>
      <p>The first four months of the program are based in Toronto at the VPI headquarters.</p>
      <p style="margin-top:8px">The curriculum we work through is highly engaging and personalized, focusing directly on students’ goals. After that, students are out in the world, achieving the remaining components of the program (e.g. internship, volunteer abroad).</p>
    </div>
  </section>

  <section class="page page--students">
    <svg class="shapes" width="533" height="705" viewBox="0 0 533 705" aria-hidden="true">
      <polygon points="0,520 190,440 533,430 533,705 0,705" fill="var(--yellow)"/>
      <polygon points="0,520 190,440 260,705 0,705" fill="var(--yellow-soft)"/>
      <polygon points="40,705 190,500 533,560 533,705" fill="var(--yellow)"/>
      <polygon points="110,620 533,470 533,560" fill="var(--yellow-pale)" opacity=".7"/>
      <polygon points="533,470 533,705 470,705" fill="var(--red)"/>
    </svg>

    <div class="page-title">The Students</div>

    <h2 class="who-title">Who’s it for</h2>
    <h3 class="group-hs">HIGH SCHOOL GRADUATES</h3>
    <p class="body" style="top:112px">90% of high school grads aren't sure why they’re going to university or what they want to study.</p>
    <p class="body" style="top:147px">VPI helps students discover what they truly want to do in life, and make enormous progress</p>
    <div class="photo" role="img" aria-label="Photo of high school students writing at a desk" style="left:400px;top:87px;width:120px;height:81px;background:linear-gradient(135deg,#c9d3df,#8b7a6a)"></div>

    <h3 class="group-head" style="top:190px">Post-secondary students</h3>
    <p class="body" style="top:219px">28% of students switch or drop out of their program because it wasn’t for them or they didn’t like it.</p>
    <p class="body" style="top:259px">Don't keep moving around or risk switching careers down the road – find out what sparks your passion with VPI.</p>
    <div class="photo" role="img" aria-label="Photo of smiling graduates in caps and gowns" style="left:400px;top:193px;width:120px;height:81px;background:linear-gradient(135deg,#9ab8d2,#2e2a30)"></div>

    <h3 class="group-head" style="top:338px">Post-secondary graduates</h3>
    <p class="body" style="top:368px">50% of graduates are unemployed or underemployed, 60% are in debt.</p>
    <p class="body" style="top:407px">VPI will help you get your dream job – our students won’t settle for anything less.</p>
    <div class="photo" role="img" aria-label="Photo of a cheering graduating class" style="left:391px;top:344px;width:129px;height:76px;background:linear-gradient(135deg,#6fa04a,#232323)"></div>

    <h2 class="apply-title">How to apply</h2>
    <span class="apply-mark"></span>
    <p class="apply-text" style="top:560px;font-size:7px">We select high-potential young leaders with a desire to improve themselves and impact the world.</p>
    <p class="apply-text" style="top:583px;font-size:8.5px">We won’t ask you for your grades – we care more about your values and potential.</p>
    <p class="apply-text" style="top:605px">Visit www.vesk.institute to apply now</p>

    <div class="badge" style="left:446px;top:614px;width:36px;height:25px;background:#e9e9e9;border:1px solid #999"></div>
    <div class="badge" style="left:485px;top:614px;width:46px;height:25px;background:#f4f4f4;border:1px solid #999"></div>
    <div class="badge" style="left:407px;top:641px;width:75px;height:24px;background:#ffffff;border:1px solid #999"></div>
    <div class="badge" style="left:485px;top:641px;width:46px;height:24px;background:var(--red);border:1px solid #999"></div>
    <div class="badge" style="left:450px;top:668px;width:81px;height:25px;background:#ffffff;border:1px solid #999"></div>
  </section>

</div>
</body>
</html>
```